Corporate Letter head and Microsoft Word Template

Brief
Design three clean, modern, professional corporate letter templates that include the BrightArc Corporation word-mark logo, company name and address and url. The designs should use one or more but no more than three tints/shades from our corporate colour pallet.
Templates should be produced in A4 and Letter formats as a Word file and should use Helvetica Now Display as the embedded font.
Design Preference:
Colour block designs, solid borders with flowing smooth lines, single side borders with connected header and footer, cut off or half page headers and footers are all acceptable.
Deliverables are:
1. Three graphic design files one for each brand logo colour and design
2. Three Word templates in 2 formats A4 and Letter
Enclosed are:
1. Three word mark logos with reverse versions of each, one for each primary brand colour.
2. BrightArc corporate colour pallet
3. BrightArc address and url
4. Helvetica Now Display font files

Target Market(s)

Professional Letter Writing to Suppliers, Customers and Authorities

Industry/Entity Type

High Tech

Font styles to use
Sans Serif
Other font styles liked:
• Helvetica Now Display

Requirements
Must have
• Clean, modern and effective design incorporating BrightArc Wordmark logo

```html
<!DOCTYPE html>
<html lang="en">
<head>
<meta charset="utf-8">
<title>BrightArc Corporation Letterhead</title>
<link rel="stylesheet" href="https://fonts.googleapis.com/css2?family=Arimo:wght@400;700&family=Montserrat:wght@400;500&display=swap">
<style>
  :root {
    --brand-blue: #3db5e6;
    --ink-dark: #2b2b2b;
    --ink-body: #8e8e8e;
    --ink-muted: #9a9a9a;
    --rule: #3a3a3a;
    --stripe-dark: #4a4a4a;
    --paper: #ffffff;
    --backdrop: #a9c7e4;
  }
  * { margin: 0; padding: 0; box-sizing: border-box; }
  html, body { width: 1200px; height: 1200px; overflow: hidden; }
  body { background: var(--backdrop); position: relative; }

  .letter {
    position: absolute; left: 190px; top: 20px;
    width: 820px; height: 1160px;
    background: var(--paper);
    font-family: "Montserrat", sans-serif;
  }

  .wordmark {
    position: absolute; left: 56px; top: 34px;
    font-family: "Arimo", sans-serif; font-weight: 700;
    font-size: 66px; line-height: 1; letter-spacing: -2px;
    color: var(--brand-blue);
  }

  .company-block {
    position: absolute; left: 535px; top: 37px;
    font-family: "Arimo", sans-serif; font-size: 14.5px; line-height: 16.6px;
    color: var(--ink-dark);
  }
  .company-block .company-name { color: var(--brand-blue); font-weight: 700; }

  .header-rule {
    position: absolute; left: 58px; top: 110px;
    width: 704px; height: 1.5px; background: var(--rule);
  }

  .recipient { position: absolute; left: 83px; top: 254px; }
  .recipient .to-label { font-size: 14px; letter-spacing: 2px; color: var(--ink-dark); }
  .recipient .recipient-name { margin-top: 7px; font-size: 13.5px; color: var(--brand-blue); }
  .recipient .recipient-line { font-size: 11px; line-height: 18px; color: var(--ink-muted); }
  .recipient .recipient-name + .recipient-line { margin-top: 6px; }

  .letter-date {
    position: absolute; right: 82px; top: 254px;
    font-size: 11.5px; color: var(--ink-dark);
  }

  .letter-body {
    position: absolute; left: 83px; top: 416px; width: 655px;
    font-size: 11.6px; line-height: 14.6px; color: var(--ink-body);
    text-align: justify;
  }
  .letter-body p + p { margin-top: 14.6px; }
  .letter-body p.short { text-align: left; }

  .signature-mark {
    position: absolute; left: 83px; top: 820px;
    width: 140px; height: 28px;
    background: linear-gradient(90deg, #e9e9e9, #f4f4f4);
    border-radius: 3px;
  }
  .signatory { position: absolute; left: 81px; top: 856px; }
  .signatory .signatory-name { font-size: 12.8px; color: var(--ink-dark); }
  .signatory .signatory-title { margin-top: 2px; font-size: 10px; color: var(--ink-muted); }

  .footer-band { position: absolute; left: 0; top: 1130px; width: 820px; height: 30px; }
  .footer-url {
    position: absolute; right: 45px; top: 1136px;
    font-family: "Arimo", sans-serif; font-size: 13.5px; color: var(--paper);
  }
</style>
</head>
<body>
  <main class="letter">
    <header>
      <div class="wordmark">BrightArc</div>
      <address class="company-block" style="font-style:normal">
        <div class="company-name">BRIGHTARC CORPORATION</div>
        <div>4820 NW Ridgeview Drive, Suite 210,</div>
        <div>Beaverton, OR 97006</div>
        <div>United States</div>
      </address>
      <div class="header-rule"></div>
    </header>

    <section class="recipient">
      <div class="to-label">TO</div>
      <div class="recipient-name">Daniel Okafor</div>
      <div class="recipient-line">Human Resources</div>
      <div class="recipient-line">Nimbus Labs Inc.</div>
      <div class="recipient-line">2207-B Harbor Lane, Eastfield</div>
      <div class="recipient-line">E41 USA</div>
    </section>

    <div class="letter-date">Friday, 01/01/2018</div>

    <article class="letter-body">
      <p>Lorem ipsum dolor sit amet, consectetuer adipiscing elit, sed diam nonmmy nibh euismod tincidunt ut laoreet dolore magna aliquam erat volutpat. Ut wisi enim ad minim veniam, quis nostrud exerci tationmcorper suscipit lobortis nisl ut aliquip ex ea commodo consequat. Duis autem vel eum iriure dolor in hendrerit in vulputate velit esse molestie consequat, vel illum dolore eu feugiat nulla facilisis at vero eros et accumsan et iusto odio dignissim qui blandit praesent luptatum zzril delenit augue duis dolore te feugait nulla facilisi.</p>
      <p>Nam liber tempor cum soluta nobis eleifend option congue nihil imprdiet doming id quod mazim placerat facer possim assum. Typi non habent claritatem insitam;</p>
      <p class="short">Est usus legentis in iis qui facit eorum claritatem.</p>
      <p>Investigationes demonstraverunt lectores legere me lius quod ii legunt saepius. Claritas est etiam processus dynamicus, qui sequitur mutationem consuetudium lectorum. Mirum est notare quam littera gothica, quam nunc putamus parum claram, anteposuerit litterarum formas humanitatis per seacula quarta decima et quinta decima. Eodem modo typi, qui nunc nobis videntur parum clari, fiant sollemnes in futurum.</p>
      <p>consectetuer adipiscing elit, sed diam nonummy nibh euismod tincidunt ut laoreet dolore magna aliquam erat volutpat. Ut wisi enim ad minim veniam, quis nostrud exerci tation ullamcorper suscipit lobortis nisl ut aliquip ex ea commodo consequat. Duis autem vel eum iriure dolor in hendrerit in vulputate velit esse molestie consequat, vel illum dolore eu feugiat nulla facilisis at vero eros et accumsan et iusto odio dignissim qui blandit praesent luptatum zzril delenit augue duis dolore te feugait nulla facilisi.</p>
      <p class="short">Nam liber tempor cum soluta nobis eleifend option congue nihil imperdiet .</p>
    </article>

    <div class="signature-mark" role="img" aria-label="Handwritten signature of Martin Hale"></div>
    <section class="signatory">
      <div class="signatory-name">Martin Hale</div>
      <div class="signatory-title">Managing Director</div>
    </section>

    <footer>
      <svg class="footer-band" viewBox="0 0 820 30" width="820" height="30" aria-hidden="true">
        <polygon points="0,7 195,7 192,12 0,12" fill="var(--stripe-dark)"/>
        <polygon points="200,7 378,7 375,12 197,12" fill="var(--brand-blue)"/>
        <polygon points="383,7 566,7 563,12 380,12" fill="var(--stripe-dark)"/>
        <path d="M0 20 L540 20 Q552 20 560 14 L572 4 Q578 0 588 0 L820 0 L820 30 L0 30 Z" fill="var(--brand-blue)"/>
      </svg>
      <div class="footer-url">www.brightarc.com</div>
    </footer>
  </main>
</body>
</html>
```